Business card for Property Management consultant

I need a business card for my business LX Vantage - I consult to real estate agents to improve the performance of their Property Management departments (rental houses management). The card needs to be very professional looking, incorporating our logo and my photo plus the line "Develop your Rent Roll to Perform"

Target Market(s)

Real Estate business owners

Industry/Entity Type

Business Consultant

Contact Information for Business Card

Business name - LX Vantage (logo uploaded)
My Name : Marcia Kellaway -
Title : Property Management Consultant

Develop your Rent Roll to perform

Phone : +61 438592716
email : marcia@lxvantage.com.au
website ; www.lxvantage.com.au

Requirements
Must have
• Logo
• My photo
• Very corporate / professional look

```html
<!DOCTYPE html>
<html lang="en">
<head>
<meta charset="utf-8">
<title>LX Vantage — Business Card</title>
<link rel="stylesheet" href="https://fonts.googleapis.com/css2?family=Open+Sans:wght@400;600&display=swap">
<style>
  :root {
    --page-bg: #ecedef;
    --card-bg: #ffffff;
    --ink: #1d1f24;
    --blue-deep: #1f5fc0;
    --blue-mid: #2f7fd3;
    --blue-light: #55aee6;
    --ring: #2a78d2;
    --icon-teal: #3aa7c9;
    --contact-gold: #d19c2e;
    --photo-top: #c9ced6;
    --photo-bottom: #8fa7c9;
  }
  * { box-sizing: border-box; margin: 0; padding: 0; }
  html, body { width: 1200px; height: 1023px; overflow: hidden; }
  body {
    background: var(--page-bg);
    font-family: "Open Sans", Arial, sans-serif;
    display: flex; align-items: center; justify-content: center;
  }
  .card {
    position: relative;
    width: 960px; height: 549px;
    background: var(--card-bg);
    border-radius: 18px;
    overflow: hidden;
    box-shadow: 0 10px 30px rgba(0,0,0,.15);
  }
  .card__wave { position: absolute; inset: 0; }
  .brand {
    position: absolute; left: 64px; top: 92px;
    display: flex; align-items: center; gap: 16px;
  }
  .brand__mark { width: 34px; height: 34px; background: var(--blue-mid); flex: none; }
  .brand__name { font-size: 64px; font-weight: 600; color: var(--ink); line-height: 1; letter-spacing: 1px; }
  .name-band {
    position: absolute; left: 0; top: 290px;
    width: 700px; height: 104px;
    background: linear-gradient(90deg, var(--blue-deep), var(--blue-mid) 60%, var(--blue-light));
    color: #fff; padding: 12px 0 0 120px;
  }
  .name-band__name { font-size: 50px; font-weight: 400; line-height: 1.05; }
  .name-band__title { font-size: 21px; font-weight: 400; margin-top: 2px; }
  .portrait {
    position: absolute; left: 560px; top: 24px;
    width: 320px; height: 320px; border-radius: 50%;
    border: 7px solid var(--ring);
    background: #fff; padding: 8px;
  }
  .portrait__fill {
    width: 100%; height: 100%; border-radius: 50%;
    background: linear-gradient(180deg, var(--photo-top), var(--photo-bottom));
  }
  .contacts { position: absolute; left: 178px; top: 418px; list-style: none; }
  .contacts li { display: flex; align-items: center; gap: 10px; font-size: 21px; color: var(--contact-gold); line-height: 34px; }
  .contacts svg { width: 20px; height: 20px; flex: none; }
</style>
</head>
<body>
  <section class="card">
    <svg class="card__wave" viewBox="0 0 960 549" aria-hidden="true">
      <defs>
        <linearGradient id="waveFill" x1="0" y1="0" x2="1" y2="1">
          <stop offset="0" stop-color="#55aee6"/>
          <stop offset="1" stop-color="#1f5fc0"/>
        </linearGradient>
      </defs>
      <path d="M700 549 C 790 500 880 470 960 380 L960 549 Z" fill="url(#waveFill)" opacity=".85"/>
      <path d="M780 549 C 850 520 910 490 960 440 L960 549 Z" fill="#1f5fc0"/>
    </svg>

    <div class="brand">
      <span class="brand__mark"></span>
      <span class="brand__name">LX Vantage</span>
    </div>

    <div class="name-band">
      <div class="name-band__name">Marcia Kellaway</div>
      <div class="name-band__title">Property Management Consultant</div>
    </div>

    <div class="portrait">
      <div class="portrait__fill" role="img" aria-label="Portrait photo of Marcia Kellaway"></div>
    </div>

    <ul class="contacts">
      <li>
        <svg viewBox="0 0 20 20" aria-hidden="true"><circle cx="10" cy="10" r="9" fill="none" stroke="var(--icon-teal)" stroke-width="2"/><path d="M7 6 l2 0 l1 2.5 -1.3 1 a6 6 0 0 0 2.8 2.8 l1-1.3 2.5 1 0 2 a1 1 0 0 1-1 1 a8 8 0 0 1-8-8 a1 1 0 0 1 1-1z" fill="var(--icon-teal)"/></svg>
        +61 438592716
      </li>
      <li>
        <svg viewBox="0 0 20 20" aria-hidden="true"><rect x="2" y="4" width="16" height="12" fill="none" stroke="var(--icon-teal)" stroke-width="1.8"/><path d="M2 4 L10 11 L18 4" fill="none" stroke="var(--icon-teal)" stroke-width="1.8"/></svg>
        marcia@lxvantage.com.au
      </li>
      <li>
        <svg viewBox="0 0 20 20" aria-hidden="true"><circle cx="10" cy="10" r="8" fill="none" stroke="var(--icon-teal)" stroke-width="1.8"/><ellipse cx="10" cy="10" rx="3.5" ry="8" fill="none" stroke="var(--icon-teal)" stroke-width="1.4"/><path d="M2 10 H18 M4 6 H16 M4 14 H16" stroke="var(--icon-teal)" stroke-width="1.2"/></svg>
        www.lxvantage.com.au
      </li>
    </ul>
  </section>
</body>
</html>
```